Meridian Swift add on sales tool2017

This will be a flyer to leave with our clients we just did work for. We want to entice them to use our other services over the next 30 days with a discount, money off etc. we will write in the special and the expiration date. I want the client to read the description and see a picture of the service they may want done.

Target Market(s)

Repeat clients

Industry/Entity Type

Cleaning Service

Font styles to use
Serif
Sans Serif

Colors
ec1f27
000000
b1b1b1

Requirements
Must have
• Call to action! look high end market, clients show we do 1st class work.
• Don't Waite
Nice to have
• Classy, quality, I'm open to using other pictures that may look better
Should not have
• Look like a typical carpet cleaners special flyer
• Not to look cluttered

```html
<!DOCTYPE html>
<html lang="en">
<head>
<meta charset="utf-8">
<title>Meridian Swift – 30 Day Special Offer</title>
<link href="https://fonts.googleapis.com/css2?family=Roboto+Condensed:wght@700&family=Open+Sans:wght@400;600;700&display=swap" rel="stylesheet">
<style>
  :root{
    --red:#ec1f27;
    --black:#000000;
    --ink:#1d1d1d;
    --grey:#b1b1b1;
    --bar-grey:#5b5b5b;
    --panel:#ececec;
    --white:#ffffff;
  }
  *{box-sizing:border-box;margin:0;padding:0}
  html,body{width:1041px;height:1200px;overflow:hidden;background:#f2f2f2}
  body{font-family:"Open Sans",sans-serif;color:var(--ink)}
  .flyer{position:relative;width:1041px;height:1200px;background:var(--white);overflow:hidden}

  /* header */
  .brand{position:absolute;left:0;top:0;width:388px;height:194px;background:var(--white);
    display:flex;align-items:center;justify-content:center}
  .brand-name{display:flex;align-items:center;gap:10px;font-family:"Open Sans",sans-serif;font-weight:700;
    font-size:28px;color:var(--red);letter-spacing:.5px}
  .brand-dot{width:22px;height:22px;border-radius:50%;background:var(--red)}

  .offer-panel{position:absolute;left:388px;top:0;width:653px;height:194px;background:var(--panel)}
  .offer-band{position:absolute;left:0;top:0;width:100%;height:58px}
  .offer-band .red-block{position:absolute;top:0;height:58px;background:var(--red)}
  .offer-band .red-block.left{left:0;width:79px}
  .offer-band .red-block.right{right:0;width:80px}
  .offer-label{position:absolute;left:84px;top:0;width:484px;height:58px;
    background:linear-gradient(#2a2a2a,#111);display:flex;align-items:center;justify-content:center;
    font-family:"Roboto Condensed",sans-serif;font-weight:700;font-size:33px;color:var(--white);letter-spacing:.5px}
  .offer-label span{color:var(--red);margin-left:10px}
  .expires{position:absolute;left:13px;bottom:8px;font-weight:700;font-size:19px;color:var(--black)}

  /* call bar */
  .call-bar{position:absolute;left:0;top:194px;width:1041px;height:62px;background:var(--bar-grey)}
  .call-label{position:absolute;left:0;top:0;width:388px;height:62px;display:flex;align-items:center;justify-content:center;
    font-family:"Roboto Condensed",sans-serif;font-weight:700;font-size:31px;color:var(--white)}
  .call-arrow{position:absolute;left:0;top:0}
  .call-phone{position:absolute;left:405px;top:0;width:300px;height:62px;display:flex;align-items:center;justify-content:center;
    font-family:"Roboto Condensed",sans-serif;font-weight:700;font-size:36px;color:var(--white)}
  .call-address{position:absolute;left:735px;top:10px;display:flex;gap:7px;color:var(--white);font-weight:600;font-size:15px;line-height:21px}
  .call-address svg{margin-top:3px;flex:none}

  /* body */
  .backdrop{position:absolute;left:0;top:256px;width:1041px;height:944px;
    background:radial-gradient(ellipse at 60% 40%,rgba(236,228,222,.55),rgba(255,255,255,0) 60%),
      linear-gradient(180deg,#f7f6f5 0%,#f1ecea 55%,#f4e9ea 80%,#f7f5f5 100%)}
  .headline{position:absolute;left:101px;top:264px;width:841px;text-align:center;
    font-family:"Roboto Condensed",sans-serif;font-weight:700;font-size:29px;color:var(--black);padding-bottom:6px}
  .headline span{color:var(--red)}
  .headline-rule{position:absolute;left:101px;top:303px;width:841px;height:2px;background:var(--red)}
  .headline-rule::after{content:"";position:absolute;left:266px;top:-1px;width:306px;height:4px;background:var(--ink)}

  .service{position:absolute}
  .service-title{display:inline-block;font-family:"Roboto Condensed",sans-serif;font-weight:700;font-size:27px;
    color:var(--black);padding:0 6px 4px 0;border-bottom:2px solid var(--ink);line-height:1.05}
  .service-title .accent{color:var(--red)}
  .service-text{margin-top:14px;font-size:18px;line-height:24px;color:#2b2b2b}

  .badge{position:absolute;width:180px;height:180px}
  .badge svg{position:absolute;left:0;top:0}
  .badge .photo{position:absolute;left:27px;top:27px;width:126px;height:126px;border-radius:50%;
    border:4px solid var(--white);box-shadow:0 2px 6px rgba(0,0,0,.25)}
</style>
</head>
<body>
<div class="flyer">

  <header>
    <div class="brand">
      <div class="brand-name"><span class="brand-dot"></span>Meridian Swift</div>
    </div>
    <div class="offer-panel">
      <div class="offer-band">
        <div class="red-block left"></div>
        <div class="offer-label">30 DAY<span>SPECIAL OFFER!</span></div>
        <div class="red-block right"></div>
      </div>
      <div class="expires">Expires</div>
    </div>
  </header>

  <div class="call-bar">
    <svg class="call-arrow" width="1041" height="62" viewBox="0 0 1041 62" aria-hidden="true">
      <polygon points="386,0 396,31 386,62 390,62 400,31 390,0" fill="#ffffff"/>
      <polygon points="396,0 706,0 724,31 706,62 396,62 406,31" fill="var(--red)"/>
      <polygon points="710,0 728,31 710,62 714,62 732,31 714,0" fill="#ffffff"/>
    </svg>
    <div class="call-label">CALL NOW TO BOOK</div>
    <div class="call-phone">702 555-0147</div>
    <div class="call-address">
      <svg width="12" height="16" viewBox="0 0 12 16" aria-hidden="true">
        <path d="M6 0C2.7 0 0 2.6 0 5.9 0 10.3 6 16 6 16s6-5.7 6-10.1C12 2.6 9.3 0 6 0zm0 8.3A2.4 2.4 0 1 1 6 3.5a2.4 2.4 0 0 1 0 4.8z" fill="#fff"/>
      </svg>
      <div>418 W. Canyon Ave. Suite B<br>702 555-0147 Las Vegas</div>
    </div>
  </div>

  <div class="backdrop" role="img" aria-label="Faded photo of a bright, elegant living room with a red patterned rug"></div>

  <h1 class="headline">ONE STOP FOR ALL YOUR HOME <span>CLEANING NEEDS</span></h1>
  <div class="headline-rule"></div>

  <!-- carpet -->
  <div class="badge" style="left:77px;top:308px">
    <svg width="180" height="180" viewBox="0 0 180 180" aria-hidden="true">
      <circle cx="90" cy="90" r="80" fill="none" stroke="var(--red)" stroke-width="15" stroke-dasharray="377 126" transform="rotate(45 90 90)"/>
    </svg>
    <div class="photo" role="img" aria-label="Photo of freshly cleaned carpeted stairs" style="background:linear-gradient(160deg,#b89a78,#e6e2dc 45%,#cfcac2)"></div>
  </div>
  <div class="service" style="left:351px;top:338px;width:600px">
    <h2 class="service-title"><span class="accent">CARPET</span> CLEANING</h2>
    <p class="service-text">Don't let dirty carpets spoil the look of your beautiful home!.<br>with 37 years of cleaning carpets experience you can expect your carpets to look like new in most cases.</p>
  </div>

  <!-- upholstery -->
  <div class="service" style="left:97px;top:500px;width:560px">
    <h2 class="service-title"><span class="accent">UPHOLSTERY</span> CLEANING</h2>
    <p class="service-text">Every day use leaves your sofa's and chairs looking dingy and can smell like dog. Our Dry cleaning, Shampoo or Rinse extraction will leave the fabric feel like clean sheet!</p>
  </div>
  <div class="badge" style="left:692px;top:472px">
    <svg width="180" height="180" viewBox="0 0 180 180" aria-hidden="true">
      <circle cx="90" cy="90" r="80" fill="none" stroke="var(--red)" stroke-width="15" stroke-dasharray="377 126" transform="rotate(45 90 90)"/>
    </svg>
    <div class="photo" role="img" aria-label="Before and after photo of a cleaned upholstered sofa" style="background:linear-gradient(90deg,#8c8f7a,#c9c6b4 48%,#fff 49%,#fff 51%,#9a8a7a 52%,#5b3e38)"></div>
  </div>

  <!-- drapery -->
  <div class="badge" style="left:77px;top:654px">
    <svg width="180" height="180" viewBox="0 0 180 180" aria-hidden="true">
      <circle cx="90" cy="90" r="80" fill="none" stroke="var(--red)" stroke-width="15" stroke-dasharray="377 126" transform="rotate(45 90 90)"/>
    </svg>
    <div class="photo" role="img" aria-label="Photo of a technician cleaning drapes in a home" style="background:linear-gradient(120deg,#7a6a5e,#c8c3bc 45%,#3a3a3a 70%,#d8d8d8)"></div>
  </div>
  <div class="service" style="left:351px;top:686px;width:600px">
    <h2 class="service-title"><span class="accent">DRAPERY</span> CLEANING</h2>
    <p class="service-text">Drapery's act like a filter attracting atmospheric soil! Making them look dingy, We make it easy to Dry clean in-home! Safe and effective beautiful drapery again.</p>
  </div>

  <!-- tile & grout -->
  <div class="service" style="left:97px;top:862px;width:560px">
    <h2 class="service-title"><span class="accent">TILE &amp; GROUT</span> CLEANING</h2>
    <p class="service-text">Tile &amp; Grout get neglected! Dirty grout can leave<br>permanent staining. Let our professionals bring back the look of a new floor.</p>
  </div>
  <div class="badge" style="left:692px;top:830px">
    <svg width="180" height="180" viewBox="0 0 180 180" aria-hidden="true">
      <circle cx="90" cy="90" r="80" fill="none" stroke="var(--red)" stroke-width="15" stroke-dasharray="377 126" transform="rotate(45 90 90)"/>
    </svg>
    <div class="photo" role="img" aria-label="Photo of tile floor half cleaned showing grout difference" style="background:linear-gradient(135deg,#6e6a66,#9a9590 50%,#c9c3ba)"></div>
  </div>

  <!-- natural stone -->
  <div class="badge" style="left:77px;top:1004px">
    <svg width="180" height="180" viewBox="0 0 180 180" aria-hidden="true">
      <circle cx="90" cy="90" r="80" fill="none" stroke="var(--red)" stroke-width="15" stroke-dasharray="377 126" transform="rotate(45 90 90)"/>
    </svg>
    <div class="photo" role="img" aria-label="Photo of a polished marble floor reflecting windows" style="background:linear-gradient(180deg,#bfc1b8,#7b7a72 45%,#55554f)"></div>
  </div>
  <div class="service" style="left:351px;top:1032px;width:600px">
    <h2 class="service-title"><span class="accent">NATURAL STONE</span><br>CLEANING &amp; POLISHING</h2>
    <p class="service-text">A dull stained Marble - Granite-Travertine and other Natural stone can be revitalized to look NEW again!</p>
  </div>

</div>
</body>
</html>
```